Church Grand Opening Bill Board design

I would like to create a bill board design for our church's grand opening. I would like to incorporate pictures of two separate preachers with a creative way of blending them both together so it won't take up too much space. I have included pictures and logo.

I am open for color coordination and I have included a couple of past designs to use as a reference

The information I would want on the Build Board is the following (1) Grand Opening (2) 4827 E. Pellford Street (3) 10:30am (4) Multi-Ethnic Church Planting Church (5) Sept. 26, 2021

Target Market(s)

Church shoppers and those who have never been connected to a church

Font styles to use
Serif

Requirements
Must have
• Our Logo
Nice to have
• i do not want any crosses or religious symbols

```html
<!DOCTYPE html>
<html lang="en">
<head>
<meta charset="utf-8">
<title>Bloomfield Church – Grand Opening Billboard</title>
<link href="https://fonts.googleapis.com/css2?family=Cinzel:wght@700&family=Crimson+Text:wght@400;600;700&display=swap" rel="stylesheet">
<style>
  :root {
    --orange: #f7931e;
    --ink: #111111;
    --white: #ffffff;
    --backdrop: #e4e4e4;
    --stage-dark: #1d1519;
    --stage-mid: #4a2f3a;
    --studio-light: #f2f2f2;
    --studio-shade: #d9d9d9;
  }
  * { margin: 0; padding: 0; box-sizing: border-box; }
  html, body {
    width: 977px; height: 1200px; overflow: hidden;
    background: var(--backdrop);
  }
  .billboard {
    position: absolute; left: 20px; top: 366px;
    width: 1364px; height: 680px;
    background: var(--white);
    overflow: hidden;
    transform: scale(0.687); transform-origin: top left;
  }
  .speakers { position: absolute; left: 0; top: 0; width: 1364px; height: 680px; }

  .brand {
    position: absolute; left: 130px; top: 95px; width: 400px;
    display: flex; align-items: center; justify-content: center; gap: 16px;
  }
  .brand-dot { width: 26px; height: 26px; border-radius: 50%; background: var(--orange); flex: none; }
  .brand-name {
    font-family: "Crimson Text", serif; font-weight: 600;
    font-size: 60px; line-height: 1; color: var(--ink);
  }

  .headline {
    position: absolute; left: 46px; top: 222px; width: 700px;
    font-family: "Cinzel", serif; font-weight: 700;
    color: var(--ink); text-align: center; line-height: 116px;
  }
  .headline span { display: block; }
  .headline .grand { font-size: 142px; letter-spacing: 2px; }
  .headline .opening { font-size: 142px; letter-spacing: -2px; }

  .address-bar {
    position: absolute; left: 68px; top: 489px; width: 658px; height: 69px;
    background: var(--orange);
    display: flex; align-items: center; gap: 14px; padding-left: 20px;
  }
  .address-bar svg { width: 28px; height: 40px; flex: none; }
  .address {
    font-family: "Crimson Text", serif; font-weight: 700;
    font-size: 47px; color: var(--ink); line-height: 1;
  }

  .traits {
    position: absolute; left: 109px; top: 578px; list-style: none;
    font-family: "Crimson Text", serif; font-size: 30px; color: var(--ink);
    line-height: 36px;
  }
  .traits li { display: flex; align-items: center; gap: 8px; }
  .traits svg { width: 26px; height: 26px; flex: none; }

  .schedule {
    position: absolute; left: 436px; top: 576px;
    display: flex; align-items: center; gap: 12px;
  }
  .schedule svg { width: 58px; height: 62px; flex: none; }
  .schedule p {
    font-family: "Crimson Text", serif; font-weight: 700;
    font-size: 31px; line-height: 34px; color: var(--ink);
  }
</style>
</head>
<body>
<main class="billboard">
  <svg class="speakers" viewBox="0 0 1364 680" xmlns="http://www.w3.org/2000/svg">
    <defs>
      <linearGradient id="stage" x1="0" y1="0" x2="1" y2="1">
        <stop offset="0" stop-color="var(--stage-mid)"/>
        <stop offset="1" stop-color="var(--stage-dark)"/>
      </linearGradient>
      <radialGradient id="studio" cx="0.5" cy="0.45" r="0.6">
        <stop offset="0" stop-color="var(--studio-light)"/>
        <stop offset="1" stop-color="var(--studio-shade)"/>
      </radialGradient>
    </defs>
    <rect class="accent-strip" x="1300" y="0" width="64" height="680" fill="var(--orange)"/>
    <circle class="accent-ring-top" cx="1171" cy="206" r="215" fill="var(--orange)"/>
    <circle class="accent-ring-bottom" cx="1061" cy="480" r="292" fill="var(--orange)"/>
    <circle class="speaker-stage" cx="1061" cy="480" r="262" fill="url(#stage)" role="img" aria-label="Photo of a preacher smiling on a stage with guitars behind him"/>
    <circle class="speaker-portrait-frame" cx="1171" cy="206" r="192" fill="var(--white)"/>
    <circle class="speaker-portrait" cx="1171" cy="206" r="188" fill="url(#studio)" role="img" aria-label="Photo of a preacher in a dark jacket wearing a headset microphone"/>
  </svg>

  <div class="brand">
    <span class="brand-dot"></span>
    <span class="brand-name">Bloomfield Church</span>
  </div>

  <h1 class="headline">
    <span class="grand">GRAND</span>
    <span class="opening">OPENING</span>
  </h1>

  <div class="address-bar">
    <svg viewBox="0 0 28 40" aria-hidden="true">
      <path d="M14 1C6.8 1 1 6.8 1 14c0 9.5 13 25 13 25s13-15.5 13-25C27 6.8 21.2 1 14 1z" fill="var(--white)"/>
      <circle cx="14" cy="14" r="5" fill="var(--orange)"/>
    </svg>
    <p class="address">4827 E. Pellford Street</p>
  </div>

  <ul class="traits">
    <li>
      <svg viewBox="0 0 26 26" aria-hidden="true"><circle cx="13" cy="13" r="12" fill="var(--orange)"/><path d="M7 13.5l4 4 8-8" fill="none" stroke="var(--white)" stroke-width="3" stroke-linecap="round" stroke-linejoin="round"/></svg>
      Planting Church
    </li>
    <li>
      <svg viewBox="0 0 26 26" aria-hidden="true"><circle cx="13" cy="13" r="12" fill="var(--orange)"/><path d="M7 13.5l4 4 8-8" fill="none" stroke="var(--white)" stroke-width="3" stroke-linecap="round" stroke-linejoin="round"/></svg>
      Multi-Ethnic Church
    </li>
  </ul>

  <div class="schedule">
    <svg viewBox="0 0 58 62" aria-hidden="true">
      <circle cx="29" cy="34" r="24" fill="none" stroke="var(--orange)" stroke-width="3"/>
      <circle cx="29" cy="34" r="19" fill="none" stroke="var(--orange)" stroke-width="1.5"/>
      <path d="M29 21v13h9" fill="none" stroke="var(--orange)" stroke-width="3" stroke-linecap="round"/>
      <circle cx="10" cy="9" r="6" fill="none" stroke="var(--orange)" stroke-width="3"/>
      <circle cx="48" cy="9" r="6" fill="none" stroke="var(--orange)" stroke-width="3"/>
      <path d="M14 57l-4 4M44 57l4 4" stroke="var(--orange)" stroke-width="3" stroke-linecap="round"/>
    </svg>
    <p>10:30am<br>Sept. 26, 2021</p>
  </div>
</main>
</body>
</html>
```